Copper Lantern Stationery Design COMMITTED PAY

We need you to design stationary for a new Business called Copper Lantern. We have already got the logo designed and it is attached. Obviously we're looking for a stationery set designed around the colours and style to match the logo.

Use generic name, address, phone, fax, email etc ... I will edit text to required details.

What we need:
- Business Card Design Double Sided (90 x 55m + Bleed 3mm+)
- A4 Letter head Design
- A4 Presentation Folder Design
- Invoice Header Approx 210 x 55mm (Include Logo & Images)

And whatever other bonuses you'd like to kick in associated with the package.

I've attached some images and I've got hundreds more. If you want something else in the way of images, let me know.

I look forward to your seeing your designs.
Updates

Thought I should just clarify the follwoing:

1. The Invoice Header is just a branding for the top of my accounting package form.  It is not contain any contact information or the like.  Just logo, some images and some of your creativity and flair to bring it together.
2. The business does synthetic grass (75% of the business), Wetpour Rubber Surfaces, Softfall Surfaces and Rubber Wood Mulch.  These are categories you might choose to somehow highlight on the letterhead.
3. Business Card reverse side should be used to highlight the categories using images provided.

Wow, I've had some really nice designs submitted thus far, but my concern is that I can't just have an awesome looking card.  I really feel that my card needs to either show or say what we do.  Please make sure your design either shows or says the following:

- Synthetic Grass
- Wetpour Rubber Surfaces
- Softfall Surfaces
- Rubber Wood Mulch
- Shade Structures
- Landscape Structures

Just another note, don't know if I mentioned it or not in the original brief, but I prefer the use of icons instead of text for phone, email, fax etc labels.

Industry/Entity Type

Business

Requirements
Must have
• - Provide full editable source files
- Provide letterhead in MS Word format as well
- All designs must be awesome, but also show or say what we do. This is very important to me. I want anyone to look at our letterhead, business card etc and know instantly what it is that we do.
- Super quick turnaround on handover. I need card files to the printer on Monday morning (that's my Monday at GMT+10)
Nice to have
• - Creative use of the logo for a little bit of wow
Should not have
• - not square, boxy or rigid ... Loosen up a bit!

```html
<!DOCTYPE html>
<html lang="en">
<head>
<meta charset="utf-8">
<title>Copper Lantern – Business Card</title>
<link href="https://fonts.googleapis.com/css2?family=Exo+2:wght@400;600;700&display=swap" rel="stylesheet">
<style>
  :root {
    --bg: #1c1c1c;
    --card-dark: #2a2a2a;
    --green: #8cc63f;
    --green-deep: #6fa82a;
    --blue: #1e9ad6;
    --white: #ffffff;
    --ink-dark: #1f2a10;
  }
  * { margin: 0; padding: 0; box-sizing: border-box; }
  html, body { width: 1200px; height: 900px; overflow: hidden; }
  body {
    background: var(--bg);
    font-family: "Exo 2", sans-serif;
    position: relative;
  }
  .card {
    position: absolute;
    left: 320px;
    width: 560px;
    height: 342px;
    border-radius: 3px;
    overflow: hidden;
    box-shadow: 0 10px 30px rgba(0,0,0,.55);
  }
  /* Front */
  .card-front { top: 60px; background: var(--card-dark); }
  .front-panel { position: absolute; inset: 0; width: 100%; height: 100%; }
  .front-text {
    position: absolute;
    right: 30px;
    top: 34px;
    text-align: right;
    color: var(--white);
  }
  .person-name { font-size: 21px; font-weight: 700; letter-spacing: .5px; }
  .person-role { font-size: 12px; margin-top: 2px; color: var(--ink-dark); font-weight: 600; }
  .address { font-size: 12px; margin-top: 14px; line-height: 1.35; color: var(--ink-dark); }
  .contacts { font-size: 12px; margin-top: 10px; line-height: 1.35; }
  .front-brand {
    position: absolute;
    right: 30px;
    bottom: 40px;
    text-align: right;
  }
  .brand-name {
    font-size: 34px;
    font-weight: 700;
    color: var(--white);
    text-transform: uppercase;
    line-height: 1;
    letter-spacing: 1px;
  }
  .brand-tagline { font-size: 11.5px; color: var(--white); margin-top: 6px; }
  /* Back */
  .card-back {
    top: 480px;
    background: var(--card-dark);
    text-align: center;
    padding-top: 92px;
  }
  .back-brand-name {
    font-size: 40px;
    font-weight: 700;
    color: var(--blue);
    text-transform: uppercase;
    letter-spacing: 1px;
    line-height: 1;
  }
  .back-tagline { font-size: 14px; font-weight: 600; color: var(--green); margin-top: 6px; }
  .services {
    list-style: none;
    margin: 44px auto 0;
    width: 470px;
    font-size: 15px;
    line-height: 1.5;
    text-align: left;
  }
  .services li { display: inline; }
  .services .blue { color: var(--blue); }
  .services .green { color: var(--green); }
  .services .sep { color: var(--white); margin: 0 4px; }
</style>
</head>
<body>

<section class="card card-front">
  <svg class="front-panel" viewBox="0 0 560 342" preserveAspectRatio="none" aria-hidden="true">
    <path d="M250 0 H560 V342 H200 C260 260 300 170 250 0 Z" fill="var(--green)"/>
    <path d="M250 0 C300 170 260 260 200 342" fill="none" stroke="var(--green-deep)" stroke-width="6"/>
  </svg>
  <div class="front-text">
    <div class="person-name">DANA WHITCOMBE</div>
    <div class="person-role">Managing Director</div>
    <div class="address">Harbour City, Eastvale,<br>P.O. Box 000000</div>
    <div class="contacts">
      P: +00 21 448 000 &nbsp;F: +00 21 448 000<br>
      E: info@CopperLantern.com<br>
      W: www.CopperLantern.com
    </div>
  </div>
  <div class="front-brand">
    <div class="brand-name">Copper Lantern</div>
    <div class="brand-tagline">Synthetic Grass &amp; Softfall Rubber Surfaces</div>
  </div>
</section>

<section class="card card-back">
  <div class="back-brand-name">Copper Lantern</div>
  <div class="back-tagline">Synthetic Grass &amp; Softfall Rubber Surfaces</div>
  <ul class="services">
    <li class="blue">Synthetic Grass</li><li class="sep">|</li>
    <li class="green">Wetpour Rubber Surfaces</li><li class="sep">|</li>
    <li class="blue">Softfall Surfaces</li><br>
    <li class="green">Rubber Wood Mulch</li><li class="sep">|</li>
    <li class="blue">Shade Structures</li><li class="sep">|</li>
    <li class="green">Landscape Structures</li>
  </ul>
</section>

</body>
</html>
```